Aviation security consulting company needs a website

We need a website design for Brisk Holloway, and aviation security consulting company. Brisk Holloway (www.briskholloway.example) is an aviation security consulting company that works with government and industry stakeholders in over 60 countries on aviation security strategy, governance, and oversight at the regulatory and operational level.
Brisk Holloway is strongly internationally focused.
The website required should be simple, corporate, serious, and communicate professionalism, reliability and honesty. We are trying to give the company a feeling of being well established.
The attached files include the company logo, along with examples of company web page styles that we like.
The Brisk Holloway website need only be around five pages long (landing page, who we are, our services, our clients, contact), though don't feel limited to only five pages.
The existing website (www.briskholloway.example) was rushed and put together using Wix. We don't love the existing website as it looks too amateur, so don't use it as a template.
There is no requirement for any online sales tools to be included in the site. The site is purely informational, with the option of people making contact via email.

```html
<!DOCTYPE html>
<html lang="en">
<head>
<meta charset="utf-8">
<title>Brisk Holloway — Aviation Security Consulting</title>
<link rel="stylesheet" href="https://fonts.googleapis.com/css2?family=Roboto:wght@300;400;500;700;900&family=PT+Serif:ital,wght@0,400;0,700;1,400&display=swap">
<style>
:root{
  --navy:#0e2a3e;
  --navy-deep:#0a2233;
  --navy-mid:#133247;
  --blue:#3d9be0;
  --blue-band:#4aa3dc;
  --ink:#1d2a35;
  --body:#4a5560;
  --muted:#8a95a0;
  --line:#d8dee4;
  --paper:#ffffff;
  --mist:#f1f4f7;
}
*{box-sizing:border-box;margin:0;padding:0}
html,body{width:1200px;height:4027px;overflow:hidden}
body{font-family:"PT Serif",Georgia,serif;color:var(--body);background:var(--paper);position:relative}
section,header,footer{position:absolute;left:0;width:1200px}

/* BRAND */
.brand{display:flex;align-items:center;gap:12px;font-family:"Roboto",Arial,sans-serif}
.brand-box{width:52px;height:52px;border:3px solid #fff}
.brand-name{font-size:30px;font-weight:500;line-height:1;color:#fff;white-space:nowrap}
.brand-tag{font-size:12px;letter-spacing:3px;color:#dfe8f0;margin-top:4px;white-space:nowrap}

/* HERO */
.hero{top:0;height:572px;background:linear-gradient(180deg,#2d4a66 0%,#4a6e8f 35%,#7e98ae 60%,#3b5670 100%);color:#fff}
.hero-photo{position:absolute;inset:0}
.nav{position:absolute;top:26px;left:34px;right:34px;display:flex;align-items:center;font-family:"Roboto",Arial,sans-serif}
.menu{display:flex;gap:34px;margin-left:auto;font-size:12px;font-weight:700;letter-spacing:.5px}
.menu a{color:#fff;text-decoration:none}
.menu a.active{color:var(--blue)}
.nav-phone{margin-left:34px;display:flex;gap:14px;align-items:center;font-size:14px;font-weight:700;white-space:nowrap}
.hero-copy{position:absolute;top:232px;left:0;right:0;text-align:center;font-family:"Roboto",Arial,sans-serif}
.hero-kicker{font-style:italic;letter-spacing:4px;font-size:15px}
.hero-title{font-size:44px;font-weight:700;line-height:1.15;margin-top:14px;letter-spacing:.5px}
.btn{display:inline-block;font-family:"Roboto",Arial,sans-serif;font-size:11px;font-weight:700;letter-spacing:1px;padding:10px 22px;color:#fff;background:var(--blue)}
.hero .btn{margin-top:26px}

/* HEADINGS */
.kicker-head{display:flex;align-items:flex-end;gap:12px;font-family:"Roboto",Arial,sans-serif;white-space:nowrap}
.kicker-head small{font-size:8px;letter-spacing:1.5px;color:var(--muted);padding-bottom:5px}
.kicker-head h2{position:relative;font-size:21px;font-weight:700;letter-spacing:2px;color:var(--ink);line-height:1}
.kicker-head h2::before{content:"";position:absolute;left:-34px;top:-10px;width:40px;height:2px;background:var(--blue)}

/* ABOUT */
.about{top:572px;height:400px}
.about-text{position:absolute;left:236px;top:80px;width:318px}
.about-text h3{font-size:16px;font-weight:700;color:var(--ink);margin:26px 0 20px}
.about-text p{font-size:12.5px;line-height:1.6;margin-bottom:16px}
.about-stack{position:absolute;left:585px;top:68px;width:400px;height:280px}
.about-stack .plate{position:absolute;width:340px;height:240px;background:var(--navy-mid)}
.about-photo{position:absolute;left:0;top:30px;width:340px;height:242px;background:linear-gradient(180deg,#4c86c4 0%,#8fb6dc 55%,#e9b47a 85%,#b58758 100%)}

/* SERVICES */
.services-head{top:972px;height:142px;background:var(--mist)}
.services-head .kicker-head{position:absolute;right:745px;top:64px}
.services-head p{position:absolute;left:483px;top:52px;width:560px;font-size:12.5px;line-height:1.55}
.grid{top:1114px;height:1123px;display:grid;grid-template-columns:repeat(3,400px);grid-template-rows:282px 282px 282px 277px}
.tile-photo{width:400px;height:100%}
.tile-text{color:#dfe7ee;text-align:center;padding:40px 44px 0;font-size:11.5px;line-height:1.45}
.tile-text h3{font-family:"Roboto",Arial,sans-serif;font-size:15px;font-weight:700;color:#fff;margin-bottom:14px}
.tone-a{background:var(--navy)}
.tone-b{background:var(--navy-mid)}

/* CLIENTS */
.clients{top:2237px;height:247px;background:var(--paper)}
.clients .kicker-head{justify-content:center;margin-top:66px}
.client-row{display:flex;justify-content:center;align-items:center;gap:22px;margin-top:48px;font-family:"Roboto",Arial,sans-serif}
.client{display:flex;align-items:center;gap:7px;font-size:12px;font-weight:700;color:var(--navy);white-space:nowrap}
.client i{display:block;width:20px;height:20px;background:var(--navy)}
.client i.round{border-radius:50%}

/* TESTIMONIALS */
.testimonials{top:2484px;height:389px;background:var(--navy-deep);color:#fff}
.testimonials .kicker-head{justify-content:center;margin-top:68px}
.testimonials .kicker-head small{color:#9fb1c0}
.testimonials .kicker-head h2{color:#fff}
.quotes{display:flex;justify-content:center;gap:30px;margin-top:44px}
.quote{width:230px;border:1px solid #26455c;padding:18px 18px 16px}
.quote-head{display:flex;align-items:center;gap:10px;margin-bottom:12px}
.avatar{width:38px;height:38px;border-radius:50%;background:linear-gradient(160deg,#c5ccd2,#7a8894)}
.quote-name{font-family:"Roboto",Arial,sans-serif;font-size:12px;font-weight:700}
.quote-role{font-size:9px;color:#9fb1c0}
.quote p{font-size:11px;line-height:1.5;color:#cfd9e2}
.dots{display:flex;justify-content:center;gap:6px;margin-top:34px}
.dots i{width:18px;height:2px;background:#4d6a80}
.dots i.on{background:#fff}

/* CONTACT */
.contact{top:2873px;height:489px}
.contact-photo{position:absolute;left:0;top:0;width:599px;height:489px;background:linear-gradient(180deg,#2b3f63 0%,#6a7ea5 30%,#e3a45f 58%,#f4d09c 72%,#8b6a56 100%)}
.contact-form{position:absolute;left:717px;top:54px;width:322px}
.contact-form h3{font-size:21px;font-weight:700;color:var(--ink);margin-bottom:16px}
.contact-form p{font-size:13px;line-height:1.55;margin-bottom:20px}
.field{font-size:11px;color:var(--muted);border-bottom:1px solid var(--line);padding:8px 0;margin-bottom:14px}
.field.tall{height:60px}
.contact-form .btn{margin-top:24px}

/* CTA */
.cta{top:3362px;height:102px;background:var(--blue-band);color:#fff;font-family:"Roboto",Arial,sans-serif}
.cta-text{position:absolute;left:236px;top:30px}
.cta-text strong{font-size:15px;font-weight:700;letter-spacing:.5px}
.cta-text span{display:block;font-size:10px;font-style:italic;margin-top:4px;opacity:.9}
.cta-btn{position:absolute;left:864px;top:36px;border:1px solid #fff;font-size:10px;font-weight:700;letter-spacing:1px;padding:7px 26px}

/* FOOTER */
.footer{top:3464px;height:563px;background:linear-gradient(180deg,#0b2334,#0e2a3e);color:#fff}
.footer-info{position:absolute;top:78px;left:0;right:0;display:flex;justify-content:center;gap:200px;font-size:11px;font-style:italic;text-align:center}
.footer-info svg{display:block;margin:0 auto 10px}
.footer-brand{position:absolute;top:235px;left:0;right:0;display:flex;justify-content:center}
.footer-sub{position:absolute;top:355px;left:0;right:0;text-align:center;font-size:10px;color:#c5d2dd}
.footer .ghost{position:absolute;top:385px;left:558px;border:1px solid #fff;font-family:"Roboto",Arial,sans-serif;font-size:9px;font-weight:700;letter-spacing:1px;padding:6px 16px}
.bottom-bar{position:absolute;bottom:0;left:0;right:0;height:32px;background:#08192a;display:flex;align-items:center;font-size:8.5px;color:#9fb1c0;padding:0 224px}
.socials{display:flex;gap:18px;margin-left:118px}
.socials i{width:8px;height:8px;border-radius:50%;background:#9fb1c0}
.legal{margin-left:auto;display:flex;gap:10px}
</style>
</head>
<body>

<header class="hero">
  <div class="hero-photo" role="img" aria-label="Passenger jet flying through a cloudy sky"></div>
  <nav class="nav">
    <div class="brand">
      <div class="brand-box"></div>
      <div>
        <div class="brand-name">Brisk Holloway</div>
        <div class="brand-tag">aviation security consulting</div>
      </div>
    </div>
    <div class="menu">
      <a class="active">HOME</a><a>WHO WE ARE</a><a>OUR SERVICES</a><a>OUR CLIENTS</a><a>TESTIMONIALS</a><a>CONTACT</a>
    </div>
    <div class="nav-phone">
      <svg width="14" height="14" viewBox="0 0 14 14"><circle cx="6" cy="6" r="4.5" fill="none" stroke="#fff" stroke-width="1.6"/><line x1="9.3" y1="9.3" x2="13" y2="13" stroke="#fff" stroke-width="1.6"/></svg>
      <svg width="14" height="14" viewBox="0 0 14 14"><path d="M3 1l2.5 3-1.4 1.6a8 8 0 0 0 4.3 4.3L10 8.5l3 2.5-1.5 2A11 11 0 0 1 1 2.5z" fill="#fff"/></svg>
      <span>(00) 123 808 800</span>
    </div>
  </nav>
  <div class="hero-copy">
    <div class="hero-kicker">WELCOME TO</div>
    <h1 class="hero-title">BRISK HOLLOWAY<br>AVIATION SECURITY CONSULTING</h1>
    <span class="btn">EXPLORE OUR SERVICES</span>
  </div>
</header>

<section class="about">
  <div class="about-text">
    <div class="kicker-head"><small>WELCOME TO</small><h2>BRISK HOLLOWAY</h2></div>
    <h3>Aviation Security Consulting</h3>
    <p>Brisk Holloway is a full service aviation security consulting company with experience in over 60 countries. We work with government and industry stakeholders to deliver outstanding security outcomes at both a regulatory and operational level.</p>
    <p>Contact us to discuss your aviation security requirements and how we can work in partnership to ensure you exceed your domestic and international aviation security obligations.</p>
  </div>
  <div class="about-stack">
    <div class="plate" style="left:50px;top:0"></div>
    <div class="plate" style="left:25px;top:15px;background:#1c4261"></div>
    <div class="about-photo" role="img" aria-label="Airliner climbing over a runway at sunset"></div>
  </div>
</section>

<section class="services-head">
  <div class="kicker-head"><small>LET US HELP YOU</small><h2>SERVICES</h2></div>
  <p>In depth knowledge built through years of experience brings the ability to deliver expertise to all areas of aviation security for industry and government stakeholders.</p>
</section>

<section class="grid">
  <div class="tile-photo" role="img" aria-label="Airport security van parked at a terminal" style="background:linear-gradient(180deg,#8fb4d8,#c9d3da 55%,#6f7a82)"></div>
  <div class="tile-photo" role="img" aria-label="Aircraft nose at a gate with ground service vehicle" style="background:linear-gradient(180deg,#9fb8cf,#d7dde2 50%,#6e7780)"></div>
  <div class="tile-photo" role="img" aria-label="Cargo container being loaded into a freighter" style="background:linear-gradient(180deg,#c9d6e2,#e3e6e8 45%,#b23a3a 62%,#7d8289)"></div>

  <div class="tile-text tone-a"><h3>Civil Aviation Authority / Regulator</h3>Aviation security regulatory agencies are required to navigate a plethora of conflicting domestic regulation, along with regional and international aviation security requirements. In addition, civil aviation authorities are required to ensure these regulations are appropriately implemented at the national level. Brisk Holloway can assist by inter alia, developing regulation and other regulatory mechanisms, training national inspectors, and developing audit and compliance assessment tools and programs.</div>
  <div class="tile-text tone-b"><h3>Airport Operations and Screening</h3>Brisk Holloway can work with airports and airport designers to ensure security is incorporated in airport designs, and is maximised within existing airport environments. Services include:<br>- Passenger screening point design and efficiency<br>audit and inspection of processes<br>access and egress<br>airport security management<br>vulnerability assessments (including front of house design)</div>
  <div class="tile-text tone-a"><h3>Air Cargo / Handling Agent</h3>Air cargo security is seeing rapid changes, with issues such as pre-loading advanced cargo information, electronic consignment security declarations, and secure supply chains becoming more important. Regulators continue to move away from 100% screening at airports towards whole of supply chain approaches incorporating more industry stakeholders. Brisk Holloway can assist air cargo operators meet aviation security obligations while ensuring facilitation and profitability are maintained.</div>

  <div class="tile-photo" role="img" aria-label="Travellers walking through an airport terminal" style="background:linear-gradient(180deg,#8c99a6,#c8ccd0 50%,#5d6670)"></div>
  <div class="tile-photo" role="img" aria-label="Operator at an airport control room console" style="background:linear-gradient(180deg,#2d3c4c,#5a6c7d 50%,#1b2632)"></div>
  <div class="tile-photo" role="img" aria-label="Security officers at a screening checkpoint" style="background:linear-gradient(180deg,#6b5a45,#a08a6a 45%,#2f2a26)"></div>

  <div class="tile-text tone-b"><h3>Capacity Development</h3>Every country is different, and while States must meet the same international standards, there is no 'one size fits all' approach. Each State must develop structures that are sustainable in their environment. Brisk Holloway has extensive experience working in partnership with developing economies to implement incremental changes to aviation security that don't just meet immediate needs, but maintain their viability over the medium and long term.</div>
  <div class="tile-text tone-a"><h3>Airline</h3>Brisk Holloway can work with airlines on security issues such as security program development, station inspection and audit, strategic guidance, and change management.</div>
  <div class="tile-text tone-b"><h3>Training</h3>Brisk Holloway has experienced aviation security trainers who can take participants through course material prepared by your organisation, or can develop training material tailored to your requirements.</div>
</section>

<section class="clients">
  <div class="kicker-head"><small>WE ARE PROUD</small><h2>OUR CLIENTS</h2></div>
  <div class="client-row">
    <div class="client"><i></i>Fairmark Risk</div>
    <div class="client"><i class="round"></i>Northgate</div>
    <div class="client"><i class="round"></i>Falcon Air</div>
    <div class="client"><i></i>Crimson Line</div>
    <div class="client"><i class="round"></i>Meridian Transport</div>
    <div class="client"><i class="round"></i>Skyward Air Council</div>
    <div class="client"><i class="round"></i>Global Aviation Bureau</div>
    <div class="client"><i class="round"></i>Harbor Border</div>
  </div>
</section>

<section class="testimonials">
  <div class="kicker-head"><small>WE ARE TRUSTED</small><h2>TESTIMONIALS</h2></div>
  <div class="quotes">
    <div class="quote">
      <div class="quote-head"><div class="avatar"></div><div><div class="quote-name">Marcus Teller</div><div class="quote-role">Security Director</div></div></div>
      <p>Lorem ipsum dolor sit amet, consectetur adipisicing elit, sed do eiusmod tempor incididunt ut labore et dolore magna.</p>
    </div>
    <div class="quote">
      <div class="quote-head"><div class="avatar"></div><div><div class="quote-name">Devon Ashby</div><div class="quote-role">Airport Manager</div></div></div>
      <p>Lorem ipsum dolor sit amet, consectetur adipisicing elit, sed do eiusmod tempor incididunt ut labore et dolore magna.</p>
    </div>
    <div class="quote">
      <div class="quote-head"><div class="avatar"></div><div><div class="quote-name">Rosa Linden</div><div class="quote-role">Cargo Operator</div></div></div>
      <p>Lorem ipsum dolor sit amet, consectetur adipisicing elit, sed do eiusmod tempor incididunt ut labore et dolore magna.</p>
    </div>
  </div>
  <div class="dots"><i class="on"></i><i></i></div>
</section>

<section class="contact">
  <div class="contact-photo" role="img" aria-label="Airliner flying above clouds at sunset"></div>
  <div class="contact-form">
    <h3>Contact us by email!</h3>
    <p>Whatever your aviation security requirements, contact us to discuss solutions appropriate to your operating environment.</p>
    <div class="field">Your Name</div>
    <div class="field">Phone number</div>
    <div class="field">Email address</div>
    <div class="field tall">Message</div>
    <span class="btn">SUBMIT FORM</span>
  </div>
</section>

<section class="cta">
  <div class="cta-text"><strong>ARE YOU INTERESTED IN COOPERATION? WRITE TO US!</strong><span>If you think it's useful and the timing fits, please contact us and share your details.</span></div>
  <div class="cta-btn">CONTACT US</div>
</section>

<footer class="footer">
  <div class="footer-info">
    <div><svg width="16" height="20" viewBox="0 0 16 20"><path d="M8 1a6 6 0 0 0-6 6c0 5 6 12 6 12s6-7 6-12a6 6 0 0 0-6-6z" fill="none" stroke="#fff" stroke-width="1.5"/><circle cx="8" cy="7" r="2" fill="#fff"/></svg>Your Address Here</div>
    <div><svg width="18" height="18" viewBox="0 0 14 14"><path d="M3 1l2.5 3-1.4 1.6a8 8 0 0 0 4.3 4.3L10 8.5l3 2.5-1.5 2A11 11 0 0 1 1 2.5z" fill="none" stroke="#fff" stroke-width="1.1"/></svg>Phone: (00) 123 908 908</div>
    <div><svg width="18" height="18" viewBox="0 0 18 18"><path d="M1 8l16-7-6 16-2-7z" fill="none" stroke="#fff" stroke-width="1.4" stroke-linejoin="round"/></svg>Email: Your email Here</div>
  </div>
  <div class="footer-brand">
    <div class="brand">
      <div class="brand-box"></div>
      <div><div class="brand-name">Brisk Holloway</div><div class="brand-tag">aviation security consulting</div></div>
    </div>
  </div>
  <div class="footer-sub">Subscribe Our Newsletter</div>
  <div class="ghost">SUBSCRIBE US</div>
  <div class="bottom-bar">
    <span>Copyright | Brisk Holloway © 2016. All Rights Reserved.</span>
    <div class="socials"><i></i><i></i><i></i><i></i></div>
    <div class="legal"><span>About</span>|<span>Customer Service</span>|<span>Terms</span>|<span>Contact</span></div>
  </div>
</footer>

</body>
</html>
```